website design for B&T Electric

A portfolio website for a high end commercial and residential electrical contracting company. The current site bandtelectric.example does not represent the current direction but the images in the gallery give you an idea of the work we do. Current logo will be uploaded shortly but is black text on white background.
Target Market(s)
General Contractors, Residential Home Owners, clients intersted in Voskal home automation.
Industry/Entity Type
Electrician
Coding
Coded - Design and coding required
Number of Pages Required
2 page
Font styles to use
Sans Serif
Colors
Designer to choose colors to be used in the design.
Requirements
Must have
- Portfolio section highlighting different service areas and products (Voskal Dwellsync, etc)

```html
<!DOCTYPE html>
<html lang="en">
<head>
<meta charset="utf-8">
<title>B&amp;T Electric</title>
<link href="https://fonts.googleapis.com/css2?family=Open+Sans:ital,wght@0,400;0,600;0,700;0,800;1,400&display=swap" rel="stylesheet">
<style>
:root{
  --red:#e8132c;
  --red-dark:#c50d22;
  --ink:#1c1c1c;
  --text:#555;
  --muted:#888;
  --line:#dcdcdc;
  --white:#fff;
}
*{box-sizing:border-box;margin:0;padding:0}
html,body{width:1200px;height:2761px;overflow:hidden;background:var(--white)}
body{font-family:"Open Sans",Arial,sans-serif;color:var(--ink);position:relative}
.abs{position:absolute}

/* hero */
.hero{position:absolute;left:0;top:0;width:1200px;height:567px;
  background:radial-gradient(ellipse at 50% 90%,#4a3a22 0%,rgba(20,22,35,0) 60%),
  linear-gradient(180deg,#05070c 0%,#151b2b 45%,#3a3120 80%,#1d1a16 100%)}
.brand{position:absolute;font-weight:400;font-size:38px;letter-spacing:1px;white-space:nowrap}
.hero .brand{left:98px;top:38px;color:#e8e8e8}
.phone-top{position:absolute;left:938px;top:14px;display:flex;align-items:center;gap:12px;color:#fff;font-size:16px;font-weight:600}
.phone-top .ring{width:30px;height:30px;border:2px solid var(--red);border-radius:50%;display:flex;align-items:center;justify-content:center}
.nav{position:absolute;top:68px;left:497px;font-size:16px;color:#fff}
.nav span{position:absolute;white-space:nowrap}
.nav .active{color:var(--red)}
.hero-title{position:absolute;top:170px;width:1200px;text-align:center;color:#fff;font-size:72px;font-weight:800;letter-spacing:1px}
.hero-sub{position:absolute;top:265px;width:1200px;text-align:center;color:#fff;font-size:26px}
.btn-hero{position:absolute;left:502px;top:331px;width:195px;height:43px;border-radius:22px;background:var(--red);color:#fff;font-size:15px;font-weight:700;display:flex;align-items:center;justify-content:center;border:2px solid #fff}
.hero-arrow{position:absolute;top:258px;width:42px;height:50px;background:rgba(0,0,0,.35);display:flex;align-items:center;justify-content:center}

/* welcome */
.welcome-title{position:absolute;left:98px;top:644px;font-size:26px;font-weight:700}
.welcome p{position:absolute;left:98px;width:455px;font-size:12.5px;line-height:24px;color:var(--text)}
.btn-outline{position:absolute;border:1.5px solid var(--red);border-radius:18px;color:var(--red);font-size:13px;font-weight:700;display:flex;align-items:center;justify-content:center;background:#fff}
.video{position:absolute;left:616px;top:629px;width:484px;height:300px;border:1px solid var(--line);padding:6px;background:#fff;box-shadow:0 1px 4px rgba(0,0,0,.15)}
.video .shot{width:100%;height:100%;background:linear-gradient(180deg,#8d939c 0%,#a8adb4 45%,#6d5e4c 70%,#4f4f4f 100%);position:relative}
.play{position:absolute;left:50%;top:50%;width:54px;height:54px;margin:-27px 0 0 -27px;border-radius:50%;background:#151515;display:flex;align-items:center;justify-content:center}

/* services */
.tile{position:absolute;top:996px;width:294px;height:276px}
.tile .label{position:absolute;left:0;bottom:0;width:100%;height:52px;display:flex;align-items:center;justify-content:space-between;padding:0 14px 0 19px;color:#fff;font-size:16px;font-weight:700;background:rgba(20,20,20,.82);white-space:nowrap}
.tile .label.hot{background:rgba(232,19,44,.88)}
.tile .go{width:22px;height:22px;border-radius:50%;background:#ddd;display:flex;align-items:center;justify-content:center;flex:none}
.tile-arrow{position:absolute;top:1110px;width:22px;height:44px;background:rgba(40,40,40,.7);display:flex;align-items:center;justify-content:center}

/* why */
.section-title{position:absolute;width:1200px;text-align:center;font-size:26px;font-weight:700}
.feature{position:absolute;top:1419px;width:216px;text-align:center}
.feature .circle{width:119px;height:119px;margin:0 auto;border:1.5px solid #cfcfcf;border-radius:50%;display:flex;align-items:center;justify-content:center}
.feature .name{margin-top:17px;font-size:18px;font-weight:600;white-space:nowrap}

/* testimonial */
.testimonial{position:absolute;left:0;top:1647px;width:1200px;height:208px;background:radial-gradient(ellipse at 50% 40%,#ff4a5a 0%,var(--red) 55%,var(--red-dark) 100%)}
.avatar{position:absolute;left:110px;top:40px;width:126px;height:126px;border-radius:50%;border:4px solid #fff;background:linear-gradient(180deg,#c9cfd6 0%,#8f9aa8 100%)}
.quote-rule{position:absolute;left:270px;top:35px;width:1px;height:140px;background:rgba(255,255,255,.8)}
.quote{position:absolute;left:304px;top:42px;width:780px;font-style:italic;font-size:14.5px;line-height:27px;color:#ffe3e6}
.author{position:absolute;left:304px;top:138px;font-size:20px;font-weight:600;color:#fff}
.t-arrow{position:absolute;top:86px}

/* blog */
.post{position:absolute;top:1997px;width:322px}
.post .thumb{height:213px;border:1px solid var(--line);padding:4px;background:#fff;position:relative}
.post .thumb .img{width:100%;height:100%}
.date{position:absolute;left:-8px;top:144px;width:46px;height:60px;background:var(--red);color:#fff;text-align:center}
.date b{display:block;font-size:22px;line-height:30px;margin-top:2px}
.date small{display:block;font-size:12px;line-height:16px}
.post h3{margin-top:22px;font-size:19px;font-weight:600}
.post p{margin-top:12px;font-size:12.5px;line-height:24px;color:var(--text)}
.post .meta{margin-top:12px;padding-top:12px;border-top:1px solid var(--line);font-size:12.5px;color:var(--text);display:flex;gap:24px}
.post .meta span{display:flex;align-items:center;gap:6px}

/* footer */
.footer-rule{position:absolute;left:0;top:2427px;width:1200px;height:4px;background:var(--red)}
.footer .brand{left:98px;top:2552px;color:#333}
.f-head{position:absolute;top:2488px;font-size:17px;font-weight:600;color:var(--ink)}
.f-links{position:absolute;left:416px;top:2528px;font-size:12.5px;color:var(--text);line-height:28px}
.f-text{position:absolute;font-size:12.5px;line-height:21px;color:var(--text)}
.email-field{position:absolute;left:585px;top:2582px;width:255px;height:32px;border-bottom:1px solid #bbb;font-size:12.5px;color:var(--muted);padding:6px 0 0 14px}
.c-row{position:absolute;left:896px;display:flex;gap:12px;font-size:12.5px;line-height:20px;color:var(--text)}
.c-row svg{flex:none;margin-top:3px}
.bottom-rule{position:absolute;left:98px;top:2690px;width:1004px;height:1px;background:var(--line)}
.copyright{position:absolute;left:98px;top:2712px;font-size:12.5px;color:var(--text)}
.social{position:absolute;top:2706px;display:flex;gap:7px;left:975px}
.social span{width:27px;height:27px;border:1.5px solid var(--red);border-radius:50%}
</style>
</head>
<body>

<header class="hero" role="img" aria-label="Night city skyline with lit skyscrapers">
  <div class="brand">B&amp;T Electric</div>
  <div class="phone-top">
    <span class="ring"><svg width="14" height="14" viewBox="0 0 24 24"><path fill="#e8132c" d="M6.6 10.8a15 15 0 0 0 6.6 6.6l2.2-2.2a1 1 0 0 1 1-.25 11.4 11.4 0 0 0 3.6.6 1 1 0 0 1 1 1V20a1 1 0 0 1-1 1A17 17 0 0 1 3 4a1 1 0 0 1 1-1h3.5a1 1 0 0 1 1 1c0 1.25.2 2.45.6 3.6a1 1 0 0 1-.25 1z"/></svg></span>
    (208) 555-0147
  </div>
  <nav class="nav">
    <span class="active" style="left:0">HOME</span>
    <span style="left:86px">GALLERY</span>
    <span style="left:191px">SPECIALTY SERVICES</span>
    <span style="left:386px">ABOUT</span>
    <span style="left:478px">CONTACT</span>
    <span style="left:591px;top:2px"><svg width="16" height="16" viewBox="0 0 24 24"><circle cx="10" cy="10" r="7" fill="none" stroke="#fff" stroke-width="3"/><path d="M15 15l7 7" stroke="#fff" stroke-width="3"/></svg></span>
  </nav>
  <h1 class="hero-title">B&amp;T ELECTRIC</h1>
  <div class="hero-sub">We are a high end commercial and residential electrical contracting</div>
  <div class="btn-hero">GET MORE INFO &gt;&gt;</div>
  <div class="hero-arrow" style="left:0"><svg width="14" height="24" viewBox="0 0 14 24"><path d="M12 2L2 12l10 10" fill="none" stroke="#ccc" stroke-width="2.5"/></svg></div>
  <div class="hero-arrow" style="right:0"><svg width="14" height="24" viewBox="0 0 14 24"><path d="M2 2l10 10L2 22" fill="none" stroke="#ccc" stroke-width="2.5"/></svg></div>
  <svg class="abs" style="left:545px;top:465px" width="110" height="102" viewBox="0 0 110 102">
    <g stroke="#fff" stroke-width="4" stroke-linecap="round">
      <path d="M55 8v8M20 24l6 6M90 24l-6 6M8 55h9M102 55h-9"/>
    </g>
    <path d="M55 30a22 22 0 0 0-13 40v10h26V70a22 22 0 0 0-13-40z" fill="none" stroke="#fff" stroke-width="6"/>
    <rect x="45" y="86" width="20" height="6" fill="#fff"/>
  </svg>
</header>

<section class="welcome">
  <h2 class="welcome-title">WELCOME TO B&amp;T ELECTRIC</h2>
  <p style="top:700px">B &amp; T Electric is a full service electrical contracting shop. We offer commercial, residential, light industrial, and agricultural services.</p>
  <p style="top:772px">We're Voskal Dwellsync and Voskal Motorized Shades certified, as well as an authorized Ravenfield generator dealer. We've served the Silver Creek and Upper Valley area for over 18 years.</p>
  <div class="btn-outline" style="left:99px;top:876px;width:124px;height:32px">READ MORE &gt;&gt;</div>
  <div class="video">
    <div class="shot" role="img" aria-label="Video still of the company's shop building">
      <div class="play"><svg width="18" height="20" viewBox="0 0 18 20"><path d="M2 1l15 9-15 9z" fill="#fff"/></svg></div>
    </div>
  </div>
</section>

<section class="services">
  <div class="tile" style="left:0;background:linear-gradient(180deg,#1f2c6b 0%,#6a7fb8 40%,#8a8fa3 70%,#4f5160 100%)" role="img" aria-label="Commercial building plaza lit at dusk">
    <div class="label hot">COMMERCIAL<span class="go"><svg width="8" height="10" viewBox="0 0 8 10"><path d="M1 1l5 4-5 4" fill="none" stroke="#e8132c" stroke-width="2"/></svg></span></div>
  </div>
  <div class="tile" style="left:302px;background:linear-gradient(180deg,#d9d7d2 0%,#a99a86 45%,#5b4636 100%)" role="img" aria-label="Modern residential kitchen with pendant lights">
    <div class="label">RESIDENTIAL<span class="go"><svg width="8" height="10" viewBox="0 0 8 10"><path d="M1 1l5 4-5 4" fill="none" stroke="#333" stroke-width="2"/></svg></span></div>
  </div>
  <div class="tile" style="left:604px;background:linear-gradient(180deg,#1d2a8a 0%,#2f3aa0 35%,#3fae4a 60%,#7a3a50 100%)" role="img" aria-label="Building facade with green LED lighting at night">
    <div class="label">LED LIGHTING<span class="go"><svg width="8" height="10" viewBox="0 0 8 10"><path d="M1 1l5 4-5 4" fill="none" stroke="#333" stroke-width="2"/></svg></span></div>
  </div>
  <div class="tile" style="left:906px;background:linear-gradient(180deg,#5a6f4c 0%,#e6e6e4 25%,#d1d1cf 70%,#9a9a98 100%)" role="img" aria-label="Standby generator units outdoors">
    <div class="label">EMERGENCY GENERATORS<span class="go"><svg width="8" height="10" viewBox="0 0 8 10"><path d="M1 1l5 4-5 4" fill="none" stroke="#333" stroke-width="2"/></svg></span></div>
  </div>
  <div class="tile-arrow" style="left:0"><svg width="10" height="16" viewBox="0 0 10 16"><path d="M8 2L2 8l6 6" fill="none" stroke="#fff" stroke-width="2"/></svg></div>
  <div class="tile-arrow" style="right:0"><svg width="10" height="16" viewBox="0 0 10 16"><path d="M2 2l6 6-6 6" fill="none" stroke="#fff" stroke-width="2"/></svg></div>
</section>

<section class="why">
  <h2 class="section-title" style="top:1342px">WHY CHOOSE B&amp;T ELECTRIC</h2>
  <div class="feature" style="left:65px">
    <div class="circle"><svg width="56" height="48" viewBox="0 0 56 48"><g fill="none" stroke="#e8132c" stroke-width="7" stroke-dasharray="5 4"><circle cx="20" cy="26" r="13"/><circle cx="43" cy="14" r="8"/><circle cx="43" cy="38" r="7"/></g><circle cx="20" cy="26" r="9" fill="#e8132c"/><circle cx="20" cy="26" r="4" fill="#fff"/></svg></div>
    <div class="name">High Performance</div>
  </div>
  <div class="feature" style="left:281px">
    <div class="circle"><svg width="36" height="52" viewBox="0 0 36 52"><path d="M18 3a15 15 0 0 0-9 27v8h18v-8A15 15 0 0 0 18 3z" fill="none" stroke="#e8132c" stroke-width="5"/><rect x="10" y="42" width="16" height="4" fill="#e8132c"/><rect x="13" y="48" width="10" height="3" fill="#e8132c"/></svg></div>
    <div class="name">Innovation</div>
  </div>
  <div class="feature" style="left:497px">
    <div class="circle"><svg width="50" height="50" viewBox="0 0 50 50"><path fill="#e8132c" d="M25 2l5 7 8-3 1 8 8 2-3 8 5 6-7 4 1 8-8 0-3 8-7-5-7 5-3-8-8 0 1-8-7-4 5-6-3-8 8-2 1-8 8 3z"/></svg></div>
    <div class="name">Reputation</div>
  </div>
  <div class="feature" style="left:713px">
    <div class="circle"><svg width="50" height="48" viewBox="0 0 50 48"><rect x="3" y="20" width="10" height="25" fill="#e8132c"/><path fill="#e8132c" d="M16 20l10-16c4 0 6 3 5 7l-2 8h14c3 0 5 3 4 6l-4 15c-1 3-3 5-6 5H16z"/></svg></div>
    <div class="name">Engineering Excellence</div>
  </div>
  <div class="feature" style="left:929px">
    <div class="circle"><svg width="54" height="44" viewBox="0 0 54 44"><path d="M19 9V4h16v5" fill="none" stroke="#e8132c" stroke-width="4"/><rect x="2" y="10" width="50" height="32" rx="4" fill="#e8132c"/><rect x="2" y="22" width="50" height="3" fill="#fff"/><rect x="23" y="19" width="8" height="9" fill="#fff"/></svg></div>
    <div class="name">Professionalism</div>
  </div>
</section>

<section class="testimonial">
  <div class="avatar" role="img" aria-label="Portrait of the client giving the testimonial"></div>
  <div class="quote-rule"></div>
  <p class="quote">Nam libero tempore, cum soluta nobis est eligendi optio cumque nihil impedit quo minus id quod maxime placeat facere possimus, omnis voluptas assumenda est, omnis dolor repellendus. Temporibus autem quibusdam et aut officiis debitis aut rerum necessitatibus saepe eveniet ut et voluptates repudiandae sint et molestiae</p>
  <div class="author">- Marcel Dufresne</div>
  <svg class="t-arrow" style="left:36px" width="16" height="30" viewBox="0 0 16 30"><path d="M14 2L2 15l12 13" fill="none" stroke="rgba(255,255,255,.7)" stroke-width="2.5"/></svg>
  <svg class="t-arrow" style="right:36px" width="16" height="30" viewBox="0 0 16 30"><path d="M2 2l12 13L2 28" fill="none" stroke="rgba(255,255,255,.7)" stroke-width="2.5"/></svg>
</section>

<section class="blog">
  <h2 class="section-title" style="top:1925px">LATEST BLOG</h2>

  <article class="post" style="left:98px">
    <div class="thumb"><div class="img" role="img" aria-label="Glowing earth with light trails" style="background:radial-gradient(circle at 30% 70%,#1f5aa8 0%,#0b1e45 45%,#03060f 100%)"></div>
      <div class="date"><b>01</b><small>NOV</small></div></div>
    <h3>Finibus Bonorum et Malorum</h3>
    <p>Nam libero tempore, cum soluta nobis est eligendi optio cumque nihil impedit quo minus id quod maxim.</p>
    <div class="meta"><span><svg width="12" height="13" viewBox="0 0 12 13"><circle cx="6" cy="3.5" r="3" fill="#e8132c"/><path d="M0 13a6 6 0 0 1 12 0z" fill="#e8132c"/></svg>John Doe</span><span><svg width="15" height="12" viewBox="0 0 15 12"><path d="M2 1h8v6H5l-3 2z" fill="none" stroke="#e8132c" stroke-width="1.5"/><path d="M11 4h3v5h-1v2l-2-2H7" fill="none" stroke="#e8132c" stroke-width="1.5"/></svg>3 Comments</span></div>
  </article>

  <article class="post" style="left:442px">
    <div class="thumb"><div class="img" role="img" aria-label="Hand touching a tablet showing charts" style="background:linear-gradient(160deg,#c7d3e2 0%,#8ea6c6 45%,#3f5f8e 100%)"></div>
      <div class="date"><b>01</b><small>NOV</small></div></div>
    <h3>Finibus Bonorum et Malorum</h3>
    <p>Nam libero tempore, cum soluta nobis est eligendi optio cumque nihil impedit quo minus id quod maxim.</p>
    <div class="meta"><span><svg width="12" height="13" viewBox="0 0 12 13"><circle cx="6" cy="3.5" r="3" fill="#e8132c"/><path d="M0 13a6 6 0 0 1 12 0z" fill="#e8132c"/></svg>John Doe</span><span><svg width="15" height="12" viewBox="0 0 15 12"><path d="M2 1h8v6H5l-3 2z" fill="none" stroke="#e8132c" stroke-width="1.5"/><path d="M11 4h3v5h-1v2l-2-2H7" fill="none" stroke="#e8132c" stroke-width="1.5"/></svg>3 Comments</span></div>
  </article>

  <article class="post" style="left:786px">
    <div class="thumb"><div class="img" role="img" aria-label="Financial charts on a screen with a pen" style="background:linear-gradient(135deg,#2a3f9a 0%,#4b6fd0 40%,#c9b04a 75%,#1c1c2a 100%)"></div>
      <div class="date"><b>01</b><small>NOV</small></div></div>
    <h3>Finibus Bonorum et Malorum</h3>
    <p>Nam libero tempore, cum soluta nobis est eligendi optio cumque nihil impedit quo minus id quod maxim.</p>
    <div class="meta"><span><svg width="12" height="13" viewBox="0 0 12 13"><circle cx="6" cy="3.5" r="3" fill="#e8132c"/><path d="M0 13a6 6 0 0 1 12 0z" fill="#e8132c"/></svg>John Doe</span><span><svg width="15" height="12" viewBox="0 0 15 12"><path d="M2 1h8v6H5l-3 2z" fill="none" stroke="#e8132c" stroke-width="1.5"/><path d="M11 4h3v5h-1v2l-2-2H7" fill="none" stroke="#e8132c" stroke-width="1.5"/></svg>3 Comments</span></div>
  </article>
</section>

<footer class="footer">
  <div class="footer-rule"></div>
  <div class="brand">B&amp;T Electric</div>

  <h4 class="f-head" style="left:416px">Information</h4>
  <div class="f-links">Home<br>Gallery<br>Specialty Services<br>About<br>Contact</div>

  <h4 class="f-head" style="left:585px">Newsletter Subscription</h4>
  <div class="f-text" style="left:585px;top:2527px;width:230px">Register your Email Address to get information about us</div>
  <div class="email-field">Email Address</div>
  <div class="btn-outline" style="left:585px;top:2628px;width:100px;height:30px;font-weight:600;font-size:12px">SUBSCRIBE</div>

  <h4 class="f-head" style="left:896px">Contact Us</h4>
  <div class="c-row" style="top:2530px"><svg width="12" height="15" viewBox="0 0 12 15"><path d="M6 0a6 6 0 0 0-6 6c0 4 6 9 6 9s6-5 6-9a6 6 0 0 0-6-6z" fill="#e8132c"/><circle cx="6" cy="6" r="2.2" fill="#fff"/></svg><span>2215 Meadow Ridge Rd, PO Box 1180<br>Larkfield, ST 00000</span></div>
  <div class="c-row" style="top:2590px"><svg width="13" height="13" viewBox="0 0 24 24"><path fill="#e8132c" d="M6.6 10.8a15 15 0 0 0 6.6 6.6l2.2-2.2a1 1 0 0 1 1-.25 11.4 11.4 0 0 0 3.6.6 1 1 0 0 1 1 1V20a1 1 0 0 1-1 1A17 17 0 0 1 3 4a1 1 0 0 1 1-1h3.5a1 1 0 0 1 1 1c0 1.25.2 2.45.6 3.6a1 1 0 0 1-.25 1z"/></svg><span>(208) 555-0147</span></div>
  <div class="c-row" style="top:2630px"><svg width="15" height="12" viewBox="0 0 15 12"><rect width="15" height="12" fill="#e8132c"/><path d="M0 0l7.5 6L15 0" fill="none" stroke="#fff" stroke-width="1.3"/></svg><span>dmorgan@bandtelectric.example<br>kreyes@bandtelectric.example</span></div>

  <div class="bottom-rule"></div>
  <div class="copyright">Copyrights © 2017, B&amp;T Electric.. All rights reserved.</div>
  <div class="social"><span></span><span></span><span></span><span></span></div>
</footer>

</body>
</html>
```